Rollway Stays

We are 100% online, promoting accommodation details and booking facilities for wheelchair dependant travellers.
Listings will only be accommodation providers which meet our specific criteria.

Target Market(s)

Wheelchair dependant people and their companions

Industry/Entity Type

Accommodation

Contact Information for Business Card

Name, mobile phone number, email address, website address

```html
<!DOCTYPE html>
<html lang="en">
<head>
<meta charset="utf-8">
<title>Rollway Stays – Business Card</title>
<link rel="stylesheet" href="https://fonts.googleapis.com/css2?family=Arimo:wght@400;700&display=swap">
<style>
  :root {
    --brand-red: #ed1c24;
    --ink: #231f20;
    --paper: #ffffff;
  }
  html, body {
    margin: 0;
    padding: 0;
    width: 1200px;
    height: 756px;
    overflow: hidden;
    background: var(--paper);
  }
  .card {
    position: relative;
    width: 1200px;
    height: 756px;
    background: var(--paper);
    font-family: "Arimo", Arial, sans-serif;
    overflow: hidden;
  }
  .red-panel {
    position: absolute;
    inset: 0;
    width: 1200px;
    height: 756px;
  }
  .brand {
    position: absolute;
    left: 40px;
    top: 372px;
    display: flex;
    align-items: center;
    gap: 26px;
  }
  .brand-dot {
    width: 62px;
    height: 62px;
    border-radius: 50%;
    background: var(--ink);
    flex: none;
  }
  .brand-name {
    margin: 0;
    color: var(--brand-red);
    font-weight: 700;
    font-size: 112px;
    line-height: 0.95;
    letter-spacing: -2px;
  }
  .contact {
    position: absolute;
    left: 980px;
    top: 424px;
    width: 170px;
    color: var(--paper);
    font-weight: 400;
  }
  .contact p { margin: 0; }
  .contact-name {
    font-size: 22px;
    line-height: 1.15;
  }
  .contact-name .given {
    letter-spacing: 3px;
  }
  .contact-role {
    font-size: 17px;
    line-height: 1.1;
  }
  .contact-email,
  .contact-web {
    font-size: 9px;
    line-height: 1.3;
  }
  .contact-address {
    margin-top: 22px !important;
    font-size: 13.5px;
    line-height: 1.3;
  }
  .contact-phones {
    margin-top: 18px !important;
    font-size: 13.5px;
    line-height: 1.3;
  }
</style>
</head>
<body>
  <main class="card">
    <svg class="red-panel" viewBox="0 0 1200 756" aria-hidden="true">
      <polygon points="569,0 1200,0 1200,756 814,756" fill="var(--brand-red)"/>
    </svg>

    <div class="brand">
      <span class="brand-dot" aria-hidden="true"></span>
      <h1 class="brand-name">Rollway<br>Stays</h1>
    </div>

    <section class="contact">
      <p class="contact-name"><span class="given">Mara</span><br>Ellison</p>
      <p class="contact-role">CEO</p>
      <p class="contact-email">mara@rollwaystays.org</p>
      <p class="contact-address">Rollway Stays,<br>14 Larkin Lane<br>Eastwood Vale, NSW 2150,<br>Australia.</p>
      <p class="contact-web">www.rollwaystays.org</p>
      <p class="contact-phones">T: (02) 5550 1200 F:<br>(02) 5550 1201 M: +61<br>3 5550 1202</p>
    </section>
  </main>
</body>
</html>
```